Need Help Rebranding My Food Blog

I have a Wordpress Food blog called BeetBuddies.com. Right now it has no life and is very bland. I am rebranding this site to a new named called, TheHoneyedPath.com. I would love to have a blog that is vibrant and full of life and personality.

One of my top priorities when a new visitor comes to my site is to quickly understand what the site is about (Gluten-free, dairy-free sweets that taste delicious).

I also want people to feel a connection with me when they come to the site.

Here are some other things that I'd like in the blog design...

1. Optin
My business is driven by adding people to my list so it is very important for me to have an optin front and center/ above-the-fold. See https://www.clevertidyearnings.com/ as an example. The headline that I would like is "Gluten-free & dairy-free sweets that actually taste good"

2. Vibrant/full life
The next important aspect of this blog is that it is vibrant. I like colors that remind me of a SUNSET. See attachments for logo and color scheme. Here's an example of a site I really like that is vibrant: http://www.sugarandopendays.com/

Also see Image titled: "Sample: Feeling". Notice the feeling you get from the image/brush strokes and how it feels light, breezy, and free spirited.

3. Food Images
The last important aspect for my blog is to showcase my recipes. I have attached a few of them as examples. Its really important for a food blog to showcase beautiful pictures of recipes for people to see so will definitely need this in the design.

Also, attached...
1. Image of me.
2. New logo for TheHoneyedPath (notice: don't use the one attached as "Sample/Feeling". That's just for reference of the feeling I like.)

Thanks!

Marion

P.S. I didn't include all the copy that would be needed so feel free to use the "lorem ipsum" text as placeholder if need be.

Target Market(s)

stay-at-home moms, dairy-free & gluten allergies, love desserts & sweets

Coding

Coded - Design and coding required

Font styles to use
Sans Serif

Requirements
Must have
• 1. Optin area with my picture and what I'm about ""Gluten-free & dairy-free sweets that actually taste good""
• 2. Must have personality/vibrancy to the site. Think full of life, not dull like my current website... beetbuddies.com
• 3. Highlight food images (Vertical image holders only)
Nice to have
• Color scheme should be based on my logo
Should not have
• No black or grey colors

```html
<!DOCTYPE html>
<html lang="en">
<head>
<meta charset="utf-8">
<title>TheHoneyedPath — Gluten-free & dairy-free sweets</title>
<link rel="stylesheet" href="https://fonts.googleapis.com/css2?family=Poiret+One&family=Mulish:wght@400;700&display=swap">
<style>
  :root {
    --sunset-pink: #e8455f;
    --sunset-orange: #ee7a45;
    --berry: #c8104f;
    --berry-deep: #a80f46;
    --blush: #fdecec;
    --field: #ecc6d6;
    --paper: #ffffff;
    --ink: #5c5058;
    --ink-strong: #3e2f37;
    --line: #e6dfe2;
    --wood-light: #e9e9e9;
    --wood-mid: #cfcfcf;
  }
  * { box-sizing: border-box; margin: 0; padding: 0; }
  html, body { width: 1106px; height: 1200px; overflow: hidden; background: var(--paper); }
  body { position: relative; font-family: "Mulish", sans-serif; color: var(--ink); }
  a { color: inherit; text-decoration: none; }

  .site-header {
    position: absolute; left: 0; top: 0; width: 1106px; height: 118px;
    background: linear-gradient(100deg, var(--sunset-pink) 0%, #ea5a55 55%, var(--sunset-orange) 100%);
  }
  .brand {
    position: absolute; left: 117px; top: 40px;
    font-family: "Poiret One", sans-serif; font-size: 26px; color: var(--paper);
  }
  .main-nav { position: absolute; top: 47px; left: 605px; display: flex; gap: 0; }
  .main-nav a {
    font-family: "Poiret One", sans-serif; font-size: 21px; color: var(--paper); margin-right: 25px;
  }
  .main-nav .caret { font-size: 11px; margin-left: 3px; }
  .search-icon { position: absolute; left: 980px; top: 47px; }

  .hero {
    position: absolute; left: 0; top: 118px; width: 1106px; height: 323px;
    background: linear-gradient(90deg, var(--wood-mid), var(--wood-light) 30%, var(--wood-mid) 60%, var(--wood-light) 85%, var(--wood-mid));
  }
  .hero-portrait {
    position: absolute; left: 0; top: 0; width: 262px; height: 323px;
    background: linear-gradient(160deg, #d9c6bd 0%, #f1e6df 55%, #e6d3cc 100%);
  }
  .hero-headline {
    position: absolute; left: 423px; top: 124px; width: 620px;
    font-family: "Poiret One", sans-serif; font-size: 39px; line-height: 36px;
    color: var(--paper); text-shadow: 0 0 2px #6a6a6a, 1px 1px 2px #6a6a6a;
  }

  .optin {
    position: absolute; left: 0; top: 441px; width: 1106px; height: 176px; background: var(--blush);
  }
  .optin-badge {
    position: absolute; left: 117px; top: 48px; display: flex; align-items: center; gap: 8px;
    font-family: "Poiret One", sans-serif; font-size: 22px; color: var(--berry);
  }
  .optin-badge .dot { width: 16px; height: 16px; border-radius: 50%; background: var(--berry); }
  .optin-title {
    position: absolute; left: 345px; top: 28px;
    font-family: "Poiret One", sans-serif; font-size: 27px; color: var(--berry);
  }
  .optin-form { position: absolute; left: 345px; top: 94px; display: flex; height: 32px; }
  .optin-form label {
    width: 80px; background: var(--blush); border: 1px solid #f6dcdf;
    font-family: "Poiret One", sans-serif; font-size: 16px; color: var(--berry);
    display: flex; align-items: center; justify-content: center;
  }
  .optin-form .email-label { width: 76px; }
  .optin-form .field { width: 190px; background: var(--field); }
  .optin-form button {
    margin-left: 10px; width: 104px; border: 0; background: var(--berry); color: var(--paper);
    font-family: "Poiret One", sans-serif; font-size: 17px; font-weight: 700;
  }

  .section-title {
    position: absolute; left: 111px; top: 694px;
    font-family: "Poiret One", sans-serif; font-size: 26px; color: var(--berry);
  }
  .recipe-card {
    position: absolute; top: 757px; width: 263px; height: 421px;
    background: var(--paper); border: 1px solid var(--line); box-shadow: 0 1px 4px rgba(120,80,100,0.12);
  }
  .recipe-card.first { left: 111px; }
  .recipe-card.second { left: 421px; }
  .recipe-photo { height: 164px; }
  .recipe-photo.cookies { background: linear-gradient(135deg, #a9a59f 0%, #ef6b6b 45%, #f2c1b8 70%, #9e9b96 100%); }
  .recipe-photo.pasta { background: linear-gradient(135deg, #e8a43a 0%, #f0c45a 40%, #d9892b 75%, #8a8a80 100%); }
  .recipe-body { padding: 17px 16px 0; }
  .recipe-title {
    font-family: "Poiret One", sans-serif; font-size: 17px; font-weight: 400; line-height: 30px;
    color: var(--berry); letter-spacing: 0.2px;
  }
  .recipe-meta { margin-top: 8px; font-size: 12.5px; font-weight: 700; line-height: 25px; color: var(--ink-strong); }
  .recipe-excerpt { font-size: 12.5px; line-height: 25px; color: var(--ink); }
  .read-more { display: block; margin-top: 8px; font-size: 12.5px; color: var(--berry); }

  .sidebar { position: absolute; left: 733px; top: 688px; width: 262px; }
  .widget-title { font-family: "Poiret One", sans-serif; font-size: 16px; font-weight: 700; color: var(--berry); }
  .search-form { display: flex; margin-top: 14px; height: 32px; border: 1px solid var(--line); }
  .search-form .field { flex: 1; }
  .search-form button { width: 57px; border: 0; background: #efe6e9; font-family: "Mulish", sans-serif; font-size: 11.5px; color: var(--ink); }
  .widget { margin-top: 64px; }
  .widget.first { margin-top: 0; }
  .widget ul { list-style: none; margin-top: 14px; }
  .widget li { font-size: 12.5px; line-height: 24.5px; margin-bottom: 7px; color: var(--ink); }
  .widget li .author { color: var(--ink-strong); }
</style>
</head>
<body>
  <header class="site-header">
    <a class="brand" href="#">TheHoneyedPath</a>
    <nav class="main-nav">
      <a href="#">Home</a>
      <a href="#">About</a>
      <a href="#">Recipes<span class="caret">&#8964;</span></a>
      <a href="#">Resources</a>
    </nav>
    <svg class="search-icon" width="16" height="16" viewBox="0 0 16 16" aria-label="Search">
      <circle cx="9.5" cy="6.5" r="5" fill="none" stroke="#fff" stroke-width="1.5"/>
      <line x1="6" y1="10" x2="1.5" y2="14.5" stroke="#fff" stroke-width="1.5"/>
    </svg>
  </header>

  <section class="hero" role="img" aria-label="Whitewashed wooden plank backdrop">
    <div class="hero-portrait" role="img" aria-label="Photo of Marion smiling, holding a plate of dairy-free chocolate pie"></div>
    <h1 class="hero-headline">Gluten-free &amp; dairy-free sweets that actually taste good</h1>
  </section>

  <section class="optin">
    <div class="optin-badge"><span class="dot"></span>TheHoneyedPath</div>
    <h2 class="optin-title">Stay Always Updated With us. Sign in with our newsletter</h2>
    <form class="optin-form">
      <label>Name</label>
      <div class="field"></div>
      <label class="email-label">Email</label>
      <div class="field"></div>
      <button type="button">Subscribe</button>
    </form>
  </section>

  <h2 class="section-title">Latest Recipies</h2>

  <article class="recipe-card first">
    <div class="recipe-photo cookies" role="img" aria-label="Heart-shaped sugar cookies with pink beet frosting"></div>
    <div class="recipe-body">
      <h3 class="recipe-title">How to Make Pink Food Coloring Naturally Using Beets</h3>
      <p class="recipe-meta">by Marion | Feb 19, 2017 | Dessert, Resources, Vegan | 0 Comments</p>
      <p class="recipe-excerpt">My daughter, Lucy’s favorite color is pink. Any shade of pink will do. Pale, dark or hot pink...</p>
      <a class="read-more" href="#">read more</a>
    </div>
  </article>

  <article class="recipe-card second">
    <div class="recipe-photo pasta" role="img" aria-label="Bowl of dairy-free macaroni and cheese"></div>
    <div class="recipe-body">
      <h3 class="recipe-title">Gluten-free &amp; Dairy-Free Mac n Cheese</h3>
      <p class="recipe-meta">by Marion | Feb 19, 2017 | Dinner, Lunch, Vegan | 0 Comments</p>
      <p class="recipe-excerpt">Growing up, one of my all time favorite lunches had to be Macaroni n’ Cheese. What’s not to love? Pasta covered in</p>
      <a class="read-more" href="#">read more</a>
    </div>
  </article>

  <aside class="sidebar">
    <div class="widget first">
      <h4 class="widget-title">Search Recipies</h4>
      <form class="search-form"><div class="field"></div><button type="button">Search</button></form>
    </div>
    <div class="widget">
      <h4 class="widget-title">Latest Recipies</h4>
      <ul>
        <li>How to Make Pink Food Coloring Naturally Using Beets</li>
        <li>Gluten-free &amp; Dairy-Free Mac n Cheese</li>
        <li>Pumpkin Chocolate Chip Cookies – Dairy-free &amp; Gluten-free</li>
      </ul>
    </div>
    <div class="widget">
      <h4 class="widget-title">Recent Comments</h4>
      <ul>
        <li><span class="author">Marion</span> on Pumpkin Chocolate Chip Cookies – Dairy-free &amp; Gluten-free</li>
        <li><span class="author">Greta</span> on Pumpkin Chocolate Chip Cookies – Dairy-free &amp; Gluten-free</li>
      </ul>
    </div>
  </aside>
</body>
</html>
```